CONTACT US Page and design for website

We need a contact us page for our website. We would like it to have a message area, a map, our information, etc.

Please see the text attachment for what we are looking for. We need to have something that is creative and interesting, modern and professional.

We believe that a contact US page should be very creative because everyone clicks that to contact us. We want it to be super professional, attention grabbing, pleasing to the eye.

PLEASE KEEP THE HEADER AND FOOTER THE SAME, ONLY THE ACTUAL CONTACT US PAGE NEEDS TO BE WORKED ON. THANKS!
We are excited to work with designers for this project.

Target Market(s)

Clients in technology business

Industry/Entity Type

Information Technology

Number of Pages Required

1 page

Font styles to use
Serif

Requirements
Must have
• CHECK THE TEXT ATTACHMENT PLEASE
• Must stay within our design colors and theme.
Nice to have
• see attachment
Should not have
• it should be special

```html
<!DOCTYPE html>
<html lang="en">
<head>
<meta charset="utf-8">
<title>Contact Us – Norvex Tech</title>
<link href="https://fonts.googleapis.com/css2?family=Open+Sans:wght@400;600;700&display=swap" rel="stylesheet">
<style>
:root{
  --teal:#14bcaa;
  --teal-dark:#0fa595;
  --ink:#3a3a3a;
  --muted:#6b6b6b;
  --line:#d8d8d8;
  --bar:#565656;
  --footer:#a6a6a6;
  --footer-bottom:#969696;
  --white:#ffffff;
  --map:#e4e4e4;
}
*{box-sizing:border-box;margin:0;padding:0}
html,body{width:954px;height:1200px;overflow:hidden}
body{position:relative;background:var(--white);font-family:'Open Sans',Arial,sans-serif;color:var(--ink)}
.abs{position:absolute}

/* header */
.brand{left:124px;top:22px;display:flex;align-items:center;gap:10px}
.brand-dot{width:34px;height:34px;border-radius:50%;background:var(--teal)}
.brand-name{font-size:22px;font-weight:600;color:var(--teal);letter-spacing:2px}
.account-tab{left:693px;top:0;width:136px;height:23px;background:#8f8f8f;border-radius:0 0 14px 14px;display:flex;overflow:hidden}
.account-tab span{flex:1;font-size:8px;color:#eee;text-align:center;line-height:23px}
.account-tab span:first-child{background:#b7b7b7;color:#555}
.head-icon{width:28px;height:28px;border-radius:50%;border:1px solid #cfe9e6;display:flex;align-items:center;justify-content:center;background:#f1fbfa}
.live-chat{left:614px;top:34px;display:flex;align-items:center;gap:6px;font-size:9.5px;color:#555}
.head-phone{left:712px;top:34px;display:flex;align-items:center;gap:7px;font-size:14px;color:#333}
.nav-rule{left:0;top:72px;width:954px;height:1px;background:#e6e6e6}
.main-nav{left:124px;top:87px;display:flex;gap:19px;font-size:7.8px;color:#444}
.search{left:688px;top:81px;width:110px;height:24px;border:1px solid #ccc;border-radius:12px;font-size:8px;color:#555;padding:0 0 0 14px;line-height:22px}
.search svg{position:absolute;right:8px;top:6px}
.basket{left:803px;top:79px;width:28px;height:28px;border-radius:50%;border:1px solid #ccc;display:flex;align-items:center;justify-content:center}
.teal-rule{left:0;top:112px;width:954px;height:2px;background:var(--teal)}

/* breadcrumb */
.crumb-bar{left:0;top:114px;width:954px;height:38px;background:var(--bar);color:var(--white);font-size:11px}
.crumb{left:124px;top:11px}
.crumb .current{color:var(--teal)}
.crumb-title{right:125px;top:10px;font-size:12.5px;font-weight:600}

/* map */
.map{left:0;top:152px;width:954px;height:318px;background:linear-gradient(90deg,#e9e9e9 0%,#e3e2df 45%,#e6e6e6 100%)}

/* contact card */
.contact-card{left:124px;top:311px;width:706px;height:230px;background:var(--teal);color:var(--white);box-shadow:0 4px 14px rgba(0,0,0,.12)}
.section-title{font-size:17.5px;font-weight:600;letter-spacing:.3px}
.section-title::after{content:"";display:block;width:51px;height:1px;background:currentColor;margin-top:3px;opacity:.8}
.contact-card .section-title{left:41px;top:33px}
.info-col{top:82px}
.info-col h3{font-size:13.5px;font-weight:600;margin-bottom:9px}
.info-col p{font-size:11px;line-height:17px;display:flex;align-items:center;gap:6px}
.stay{left:46px;top:178px;font-size:13px;font-weight:600}
.socials{display:flex;gap:6px}
.socials i{display:block;width:26px;height:26px;border-radius:50%;border:1px solid rgba(255,255,255,.85)}
.socials i.active{background:var(--white)}
.card-socials{left:175px;top:173px}

/* form */
.main-block .section-title{color:#444}
.touch-title{left:165px;top:565px}
.field{border:1px solid #cfcfcf;font-size:9px;color:#aaa;padding:8px 9px}
.submit{left:165px;top:736px;width:89px;height:26px;background:var(--teal);color:var(--white);font-size:10px;font-weight:600;text-align:center;line-height:26px}
.hours-title{left:165px;top:792px}
.hours{left:165px;top:840px;font-size:10.5px;color:#444}
.hours b{font-weight:600}
.service{left:164px;top:863px;font-size:13.5px;color:#444;display:flex;align-items:center;gap:6px}
.service .num{color:var(--teal);font-weight:600}

/* footer */
.footer{left:0;top:917px;width:954px;height:233px;background:var(--footer);color:var(--white)}
.foot-brand{left:124px;top:40px;display:flex;align-items:center;gap:9px}
.foot-brand .brand-dot{background:var(--white);width:30px;height:30px}
.foot-brand .brand-name{color:var(--white);font-size:19px}
.foot-about{left:124px;top:84px;width:244px;font-size:11px;line-height:14px}
.foot-head{font-size:13.5px;font-weight:600}
.quick{left:426px;top:46px}
.quick ul{list-style:none;margin-top:11px;font-size:10.5px;line-height:17.2px}
.foot-contact{left:579px;top:46px;font-size:10.5px}
.foot-contact .row{display:flex;align-items:center;gap:6px;margin-top:12px}
.foot-contact .big{font-size:13px;font-weight:600;margin-top:8px}
.foot-contact .mail{margin-top:2px}
.foot-socials{left:579px;top:152px}
.bottom-bar{left:0;top:1150px;width:954px;height:50px;background:var(--footer-bottom);color:var(--white)}
.copyright{left:124px;top:16px;font-size:11px;display:flex;align-items:center;gap:8px}
.copyright i{display:block;width:14px;height:14px;border-radius:50%;background:#ddd}
.legal{left:426px;top:19px;font-size:9.5px}
.legal .current{color:var(--teal)}
</style>
</head>
<body>

<header>
  <div class="abs brand"><span class="brand-dot"></span><span class="brand-name">NORVEX TECH</span></div>
  <div class="abs account-tab"><span>SIGN UP</span><span>LOGIN</span></div>
  <div class="abs live-chat">
    <span class="head-icon"><svg width="12" height="11" viewBox="0 0 12 11"><path d="M1 1h10v6H5l-3 3V7H1z" fill="#14bcaa"/></svg></span>LIVE CHAT
  </div>
  <div class="abs head-phone">
    <span class="head-icon"><svg width="11" height="11" viewBox="0 0 24 24"><path d="M6.6 10.8a15 15 0 006.6 6.6l2.2-2.2a1 1 0 011-.25 11 11 0 003.6.6 1 1 0 011 1V20a1 1 0 01-1 1A17 17 0 013 4a1 1 0 011-1h3.5a1 1 0 011 1 11 11 0 00.6 3.6 1 1 0 01-.25 1z" fill="#14bcaa"/></svg></span>555-204-7810
  </div>
  <div class="abs nav-rule"></div>
  <nav class="abs main-nav">
    <span>SERVERS</span><span>WORKSTATIONS</span><span>COMPONENTS</span><span>VIRTUAL REALITY</span><span>DRONES</span><span>ABOUT US</span><span>BLOG</span><span>RESOURCES</span><span>CONTACT US</span>
  </nav>
  <div class="abs search">Search
    <svg width="11" height="11" viewBox="0 0 12 12"><circle cx="5" cy="5" r="3.8" fill="none" stroke="#14bcaa" stroke-width="1.6"/><path d="M8 8l3 3" stroke="#14bcaa" stroke-width="1.6"/></svg>
  </div>
  <div class="abs basket"><svg width="13" height="11" viewBox="0 0 13 11"><path d="M1 4h11l-1.5 6h-8z" fill="none" stroke="#14bcaa" stroke-width="1.3"/><path d="M4 4l2-3M9 4L7 1" stroke="#14bcaa" stroke-width="1.2"/></svg></div>
  <div class="abs teal-rule"></div>
</header>

<div class="abs crumb-bar">
  <div class="abs crumb">Home &nbsp;/&nbsp; <span class="current">Contact Us</span></div>
  <div class="abs crumb-title">Contact Us</div>
</div>

<div class="abs map" role="img" aria-label="Street map showing the office location at 4820 Larkin Ave"></div>

<section class="abs contact-card">
  <h2 class="abs section-title">CONTACT INFO</h2>
  <div class="abs info-col" style="left:41px">
    <h3>Address</h3>
    <p>Norvex Tech, LLC. 4820 Larkin Ave</p>
    <p>Westfield, CA 91420</p>
  </div>
  <div class="abs info-col" style="left:234px">
    <h3>General Inquiries</h3>
    <p><svg width="9" height="9" viewBox="0 0 24 24"><path d="M6.6 10.8a15 15 0 006.6 6.6l2.2-2.2a1 1 0 011-.25 11 11 0 003.6.6 1 1 0 011 1V20a1 1 0 01-1 1A17 17 0 013 4a1 1 0 011-1h3.5a1 1 0 011 1 11 11 0 00.6 3.6 1 1 0 01-.25 1z" fill="#fff"/></svg>(555)204-7810</p>
    <p><svg width="9" height="7" viewBox="0 0 9 7"><rect width="9" height="7" fill="#fff"/><path d="M0 0l4.5 3.5L9 0" fill="none" stroke="#14bcaa"/></svg>info@norvextech.com</p>
  </div>
  <div class="abs info-col" style="left:379px">
    <h3>Sales Inquiries</h3>
    <p><svg width="9" height="9" viewBox="0 0 24 24"><path d="M6.6 10.8a15 15 0 006.6 6.6l2.2-2.2a1 1 0 011-.25 11 11 0 003.6.6 1 1 0 011 1V20a1 1 0 01-1 1A17 17 0 013 4a1 1 0 011-1h3.5a1 1 0 011 1 11 11 0 00.6 3.6 1 1 0 01-.25 1z" fill="#fff"/></svg>(555)204-7810</p>
    <p><svg width="9" height="7" viewBox="0 0 9 7"><rect width="9" height="7" fill="#fff"/><path d="M0 0l4.5 3.5L9 0" fill="none" stroke="#14bcaa"/></svg>sales@norvextech.com</p>
  </div>
  <div class="abs info-col" style="left:522px">
    <h3>Purchasing Inquiries</h3>
    <p><svg width="9" height="9" viewBox="0 0 24 24"><path d="M6.6 10.8a15 15 0 006.6 6.6l2.2-2.2a1 1 0 011-.25 11 11 0 003.6.6 1 1 0 011 1V20a1 1 0 01-1 1A17 17 0 013 4a1 1 0 011-1h3.5a1 1 0 011 1 11 11 0 00.6 3.6 1 1 0 01-.25 1z" fill="#fff"/></svg>(555)204-7811</p>
    <p><svg width="9" height="7" viewBox="0 0 9 7"><rect width="9" height="7" fill="#fff"/><path d="M0 0l4.5 3.5L9 0" fill="none" stroke="#14bcaa"/></svg>purchasing@norvextech.com</p>
  </div>
  <div class="abs stay">Stay Connected</div>
  <div class="abs socials card-socials"><i></i><i class="active"></i><i></i><i></i></div>
</section>

<main class="main-block">
  <h2 class="abs section-title touch-title">GET IN TOUCH</h2>
  <div class="abs field" style="left:165px;top:620px;width:199px;height:25px">Name :</div>
  <div class="abs field" style="left:378px;top:620px;width:199px;height:25px">E-mail :</div>
  <div class="abs field" style="left:590px;top:620px;width:199px;height:25px">Phone :</div>
  <div class="abs field" style="left:165px;top:659px;width:624px;height:64px">Message :</div>
  <div class="abs submit">Submit</div>

  <h2 class="abs section-title hours-title">HOURS OF OPERATION</h2>
  <p class="abs hours"><b>Monday To Friday :</b> 8:00am- 5:00pm</p>
  <p class="abs service">Our customer service available 24/7
    <svg width="10" height="12" viewBox="0 0 10 12"><rect x="1.5" y="0.5" width="7" height="11" rx="1.5" fill="none" stroke="#14bcaa" stroke-width="1.3"/></svg>
    <span class="num">555-204-7810</span></p>
</main>

<footer class="abs footer">
  <div class="abs foot-brand"><span class="brand-dot"></span><span class="brand-name">NORVEX TECH</span></div>
  <p class="abs foot-about">Based in Westfield California, Norvex Tech offers custom servers, storage, and workstations for local businesses in Los Angeles, Beverly Hills, Thousand Oaks, Ventura, Orange County, Santa Barbara, Oxnard, Irvine, Anaheim, and San Diego. Norvex Tech also offers such products to clients throughout the United States and Worldwide.</p>
  <div class="abs quick">
    <h3 class="foot-head">Quick Links</h3>
    <ul><li>Computer Hardware</li><li>Drones</li><li>Virtual Reality</li><li>About Us</li><li>Customer Support</li></ul>
  </div>
  <div class="abs foot-contact">
    <h3 class="foot-head">Contact Us</h3>
    <div class="row"><svg width="8" height="11" viewBox="0 0 8 11"><path d="M4 0a4 4 0 014 4c0 3-4 7-4 7S0 7 0 4a4 4 0 014-4z" fill="#fff"/><circle cx="4" cy="4" r="1.4" fill="#a6a6a6"/></svg>4820 Larkin Ave. Westfield, CA 91420</div>
    <div class="row big"><svg width="10" height="10" viewBox="0 0 24 24"><path d="M6.6 10.8a15 15 0 006.6 6.6l2.2-2.2a1 1 0 011-.25 11 11 0 003.6.6 1 1 0 011 1V20a1 1 0 01-1 1A17 17 0 013 4a1 1 0 011-1h3.5a1 1 0 011 1 11 11 0 00.6 3.6 1 1 0 01-.25 1z" fill="#fff"/></svg>555-204-7810</div>
    <div class="mail">sales@norvextech.com</div>
  </div>
  <div class="abs socials foot-socials"><i></i><i class="active"></i><i></i><i></i></div>
</footer>

<div class="abs bottom-bar">
  <div class="abs copyright"><i></i>Norvex Tech, LLC. Copyright © 2017.</div>
  <div class="abs legal">Terms and Conditions &nbsp;/&nbsp; Warranty &nbsp;/&nbsp; Information &nbsp;/&nbsp; <span class="current">Contact Us</span> &nbsp;/&nbsp; Return Policy</div>
</div>

</body>
</html>
```